KRV 2417 BELWICK AIRPORT Gliders and Jubilee

Design a poster to promote an event at our airport. We host a pancake and sausage breakfast every year to promote aviation at our airport. About 2000 people attend. The theme here at the airport definitely steers toward classic 1950s looks. We decorate with a lot of WWII aircraft and pin up girls. NO TOO RISKE' Tho, as it is a family event. I was thinking something with a K4 Merlow. I would need a blank spot at the bottom for pasting in sponsorship logos. I've attached the last 3 years flyers for reference. The date is June 8, 2025 from 8:30 am to noon.

Target Market(s)

All (family friendly)

Industry/Entity Type

Aviation

Requirements
Must have
• A 1950s theme with an airplane
Nice to have
• K4 Merlow or R27 Brisbow, Pin up girl
Should not have
• A pin up girl that shows too much skin.

```html
<!DOCTYPE html>
<html lang="en">
<head>
<meta charset="utf-8">
<title>Belwick Fly-In Poster</title>
<link rel="stylesheet" href="https://fonts.googleapis.com/css2?family=Archivo+Black&family=Oswald:wght@400;500;700&display=swap">
<style>
  :root {
    --frame-blue: #0038b0;
    --paper: #ffffff;
    --ink: #111111;
    --accent-red: #ff0000;
    --chapter-coral: #ff6347;
    --bar-grey: #333333;
    --plane-orange: #f0a868;
    --plane-green: #1a3e3e;
  }
  html, body {
    margin: 0;
    padding: 0;
    width: 849px;
    height: 1200px;
    overflow: hidden;
    background: var(--paper);
  }
  .poster {
    display: block;
    width: 849px;
    height: 1200px;
  }
  .frame-outer { fill: var(--frame-blue); }
  .frame-paper { fill: var(--paper); }
  .frame-rule { fill: none; stroke: var(--frame-blue); stroke-width: 4; }
  .star { fill: var(--frame-blue); }
  .event-title {
    font-family: "Archivo Black", "Arial Black", sans-serif;
    font-size: 178px;
    fill: var(--ink);
  }
  .event-title .title-accent { fill: var(--accent-red); }
  .event-date {
    font-family: "Oswald", "Arial Narrow", sans-serif;
    font-weight: 500;
    font-size: 108px;
    fill: #1a1a1a;
  }
  .event-date .date-accent { fill: var(--accent-red); font-weight: 700; }
  .date-bar { fill: var(--bar-grey); }
  .banner { fill: var(--frame-blue); }
  .venue-name {
    font-family: "Oswald", "Arial Narrow", sans-serif;
    font-weight: 700;
    font-size: 110px;
    fill: var(--paper);
  }
  .chapter-name {
    font-family: "Oswald", "Arial Narrow", sans-serif;
    font-weight: 500;
    font-size: 92px;
    fill: var(--chapter-coral);
  }
  .event-tagline {
    font-family: "Oswald", "Arial Narrow", sans-serif;
    font-weight: 700;
    font-size: 100px;
    fill: var(--ink);
  }
  .sponsor-rule { fill: var(--frame-blue); }
</style>
</head>
<body>
<svg class="poster" viewBox="0 0 1624 2296" xmlns="http://www.w3.org/2000/svg">
  <defs>
    <symbol id="star-shape" viewBox="-1 -1 2 2">
      <polygon points="0,-1 0.2245,-0.309 0.951,-0.309 0.363,0.118 0.588,0.809 0,0.382 -0.588,0.809 -0.363,0.118 -0.951,-0.309 -0.2245,-0.309"/>
    </symbol>
    <linearGradient id="plane-tones" x1="0" y1="0" x2="1" y2="1">
      <stop offset="0" stop-color="#f0a868"/>
      <stop offset="0.55" stop-color="#d99a62"/>
      <stop offset="1" stop-color="#1a3e3e"/>
    </linearGradient>
  </defs>

  <!-- frame -->
  <rect class="frame-outer" x="0" y="0" width="1624" height="2296"/>
  <rect class="frame-paper" x="36" y="36" width="1552" height="2224"/>
  <rect class="frame-rule" x="56" y="56" width="1512" height="2184"/>

  <!-- headline -->
  <text class="event-title" x="115" y="297" textLength="1360" lengthAdjust="spacingAndGlyphs">BELWICK FLY - <tspan class="title-accent">IN</tspan></text>

  <!-- date block -->
  <g class="date-stars">
    <use class="star" href="#star-shape" x="167" y="365" width="90" height="90"/>
    <use class="star" href="#star-shape" x="290" y="418" width="52" height="52"/>
    <use class="star" href="#star-shape" x="390" y="456" width="32" height="32"/>
    <use class="star" href="#star-shape" x="1360" y="365" width="90" height="90"/>
    <use class="star" href="#star-shape" x="1274" y="418" width="52" height="52"/>
    <use class="star" href="#star-shape" x="1194" y="456" width="32" height="32"/>
  </g>
  <text class="event-date" x="510" y="444" textLength="622" lengthAdjust="spacingAndGlyphs">SUNDAY <tspan class="date-accent">8:30am</tspan></text>
  <text class="event-date" x="510" y="535" textLength="602" lengthAdjust="spacingAndGlyphs">08, JUNE- <tspan class="date-accent">2025</tspan></text>
  <rect class="date-bar" x="517" y="560" width="596" height="24"/>

  <!-- hero illustration area -->
  <rect x="135" y="695" width="1345" height="675" rx="120" fill="url(#plane-tones)" opacity="0.85"
        role="img" aria-label="Illustration of a vintage orange and dark green biplane in flight"/>

  <!-- venue banner -->
  <path class="banner" d="M155,1540 Q810,1405 1470,1540 L1350,1610 L1430,1715 Q810,1595 195,1715 L275,1610 Z"/>
  <text class="venue-name" x="495" y="1610" textLength="636" lengthAdjust="spacingAndGlyphs">Belwick Airport</text>

  <!-- organiser and tagline -->
  <text class="chapter-name" x="510" y="1763" textLength="618" lengthAdjust="spacingAndGlyphs">KRV CHAPTER 2417</text>
  <g class="tagline-stars">
    <use class="star" href="#star-shape" x="126" y="1852" width="38" height="38"/>
    <use class="star" href="#star-shape" x="218" y="1830" width="60" height="60"/>
    <use class="star" href="#star-shape" x="332" y="1798" width="96" height="96"/>
    <use class="star" href="#star-shape" x="1212" y="1798" width="96" height="96"/>
    <use class="star" href="#star-shape" x="1360" y="1830" width="60" height="60"/>
    <use class="star" href="#star-shape" x="1476" y="1852" width="38" height="38"/>
  </g>
  <text class="event-tagline" x="455" y="1872" textLength="727" lengthAdjust="spacingAndGlyphs">Gliders &amp; Jubilee</text>

  <!-- sponsor area divider -->
  <path class="sponsor-rule" d="M135,1970 Q812,1962 1490,1970 Q812,1978 135,1970 Z"/>
</svg>
</body>
</html>
```